New letter head for Air Conditioning business

We need a new professional letter head design to suit our new re-branded air conditioning business. Our new logo is attached

```html
<!DOCTYPE html>
<html lang="en">
<head>
<meta charset="utf-8">
<title>Norvale Letterhead</title>
<link href="https://fonts.googleapis.com/css2?family=Noto+Sans:wght@400;600&family=Dancing+Script&display=swap" rel="stylesheet">
<style>
  :root {
    --backdrop: #c8e8de;
    --paper: #e9e8ea;
    --charcoal: #3a3a3d;
    --green: #4e9e6c;
    --accent-red: #d9463a;
    --icon-red: #d0121b;
    --ink: #2b2b2b;
  }
  * { margin: 0; padding: 0; box-sizing: border-box; }
  html, body { width: 1200px; height: 1012px; overflow: hidden; background: var(--backdrop); }
  body { font-family: "Noto Sans", sans-serif; color: var(--ink); }

  .letterhead {
    position: absolute; left: 265px; top: 25px;
    width: 670px; height: 961px;
    background: var(--paper);
    overflow: hidden;
  }
  .frame { position: absolute; inset: 0; }

  .brand {
    position: absolute; top: 72px; left: 0; right: 0;
    display: flex; justify-content: center; align-items: center; gap: 14px;
  }
  .brand-mark { width: 30px; height: 30px; background: var(--green); }
  .brand-name { font-size: 38px; font-weight: 600; letter-spacing: 3px; color: var(--charcoal); line-height: 1; }

  .sender { position: absolute; left: 46px; top: 169px; }
  .sender-name { font-size: 15px; color: var(--accent-red); line-height: 18px; }
  .sender-role { font-size: 13.5px; line-height: 16px; }

  .contact-list { position: absolute; left: 46px; top: 236px; list-style: none; font-size: 13px; }
  .contact-list li { height: 24.5px; line-height: 18px; }
  .contact-list .key { display: inline-block; width: 18px; }

  .letter-date { position: absolute; right: 66px; top: 285px; font-size: 13px; line-height: 18px; }

  .letter-body { position: absolute; left: 46px; top: 334px; width: 590px; font-size: 12.4px; line-height: 16.2px; white-space: nowrap; }
  .letter-body p + p { margin-top: 16.2px; }

  .closing { position: absolute; left: 46px; top: 728px; font-size: 13px; line-height: 18px; }
  .signature { font-family: "Dancing Script", cursive; font-size: 23px; line-height: 26px; margin-top: 8px; }
  .closing-role { line-height: 14px; }

  .footer-contacts { position: absolute; left: 61px; top: 866px; display: flex; align-items: center; font-size: 13.5px; line-height: 17px; }
  .footer-item { display: flex; align-items: center; }
  .footer-item + .footer-item { margin-left: 0; }
  .footer-icon { width: 32px; height: 32px; background: var(--icon-red); display: flex; align-items: center; justify-content: center; flex: none; }
  .footer-icon svg { width: 20px; height: 20px; }
  .footer-phone { width: 201px; }
  .footer-phone .footer-text { margin-left: 12px; }
  .footer-web { width: 201px; }
  .footer-web .footer-text { margin-left: 14px; }
  .footer-address .footer-text { margin-left: 17px; }
</style>
</head>
<body>
<main class="letterhead">
  <svg class="frame" width="670" height="961" viewBox="0 0 670 961" aria-hidden="true">
    <path fill="var(--charcoal)" d="M0 0 H670 V357 C662 346 643 346 643 328 V76 A45 45 0 0 0 598 31 H28 Q4 31 0 8 Z"/>
    <path fill="var(--green)" d="M0 603 Q30 603 30 640 V870 A61 61 0 0 0 91 931 H640 Q670 931 670 952 V961 H0 Z"/>
  </svg>

  <header class="brand">
    <span class="brand-mark"></span>
    <span class="brand-name">NORVALE</span>
  </header>

  <section class="sender">
    <div class="sender-name">DANIEL REYES</div>
    <div class="sender-role">Chief Director</div>
  </section>

  <ul class="contact-list">
    <li><span class="key">A</span>: Your Address Here</li>
    <li><span class="key">W</span>: Urwebsite.com</li>
    <li><span class="key">P</span>: +60 123 456</li>
  </ul>

  <div class="letter-date">Date : 09 June,2021</div>

  <article class="letter-body">
    <p>Lorem ipsum dolor sit amet, consectetur adipiscing elit, sed do eiusmod tempor incidi-<br>dunt ut labore et dolore magna aliqua. Sed viverra tellus in hac habitasse platea. Quis-<br>que non tellus orci ac auctor. Ut venenatis tellus in metus vulputate.</p>
    <p>Lacus vestibulum sed arcu non odio euismod lacinia at. Posuere lorem ipsum dolor sit<br>amet consectetur adipiscing. Consequat ac felis donec et odio pellentesque. Et leo duis<br>ut diam quam nulla porttitor massa. Purus semper eget duis at. In eu mi bibendum<br>neque. Pulvinar etiam non quam lacus suspendisse faucibus interdum posuere. Nisl<br>pretium fusce id velit ut tortor. Enim praesent elementum facilisis leo vel fringilla est.<br>Odio pellentesque diam volutpat commodo sed egestas egestas. Diam quis enim lobor-<br>tis scelerisque fermentum. Odio facilisis mauris sit amet massa vitae. Purus faucibus<br>ornare suspendisse sed. Viverra orci sagittis eu volutpat odio facilisis mauris.</p>
    <p>Ridiculus mus mauris vitae ultricies leo integer malesuada. Id cursus metus aliquam<br>eleifend. Euismod elementum nisi quis eleifend. Sem viverra aliquet eget sit. Eu<br>ultrices vitae auctor eu augue ut lectus arcu. Malesuada bibendum arcu vitae elemen-<br>tum curabitur. A arcu cursus vitae congue mauris rhoncus aenean vel elit. Quam ele-<br>mentum pulvinar etiam non. Pellentesque pulvinar pellentesque habitant morbi tris-<br>tique senectus et. Dignissim cras tincidunt lobortis feugiat vivamus at augue. Morbi<br>blandit cursus risus at. Sagittis eu volutpat odio facilisis mauris. Habitasse platea dic-<br>tumst quisque sagittis purus sit amet volutpat. Faucibus interdum posuere lorem<br>ipsum dolor sit amet consectetur adipiscing. Nulla pharetra diam sit amet nisl suscipit.</p>
  </article>

  <section class="closing">
    <div>Regards</div>
    <div class="signature">Your name</div>
    <div class="closing-role">Chief Director</div>
  </section>

  <footer class="footer-contacts">
    <div class="footer-item footer-phone">
      <span class="footer-icon">
        <svg viewBox="0 0 24 24"><path fill="#fff" d="M6.6 10.8a15.1 15.1 0 0 0 6.6 6.6l2.2-2.2c.3-.3.7-.4 1-.2 1.1.4 2.3.6 3.6.6.6 0 1 .4 1 1V20c0 .6-.4 1-1 1C10.6 21 3 13.4 3 4c0-.6.4-1 1-1h3.5c.6 0 1 .4 1 1 0 1.3.2 2.5.6 3.6.1.3 0 .7-.2 1z"/></svg>
      </span>
      <span class="footer-text">+60 1234 567<br>+60 1234 567</span>
    </div>
    <div class="footer-item footer-web">
      <span class="footer-icon">
        <svg viewBox="0 0 24 24" fill="none" stroke="#fff" stroke-width="1.5"><circle cx="12" cy="12" r="9"/><ellipse cx="12" cy="12" rx="4" ry="9"/><path d="M3 12h18M4.5 7.5h15M4.5 16.5h15"/></svg>
      </span>
      <span class="footer-text">Urname@email.com<br>Urwebsitename.com</span>
    </div>
    <div class="footer-item footer-address">
      <span class="footer-icon">
        <svg viewBox="0 0 24 24" fill="none" stroke="#fff" stroke-width="1.6"><path d="M12 17s-5-5.2-5-9a5 5 0 0 1 10 0c0 3.8-5 9-5 9z"/><circle cx="12" cy="8" r="1.8"/><ellipse cx="12" cy="19.5" rx="4.5" ry="1.5"/></svg>
      </span>
      <span class="footer-text">Your Address here</span>
    </div>
  </footer>
</main>
</body>
</html>
```